Tarrow Water Taxi and Transport Flyer

I need a business flyer for my new water taxi and freight transport business I have started here in Kodiak Alaska. Kodiak is a remote island in the middle of the gulf of Alaska. There are seven native villages around the island and Kodiak is the #2 fishing port in the United States. We also have the largest Coast Guard Base in the U.S.
My company will be providing water taxi and freight transport logistics to the villages and many hunting and fishing lodges as well as remote properties around the island.

I would like a business flyer that isn't status quo, something that stands out. I do like clean minimal designs but it needs to have the necessary contact info on it.

Target Market(s)

remote lodge / property owners, residents of the many villages around the island and anyone wanting to enjoy the great outdoors of Kodiak Alaska

Industry/Entity Type

Business

Colors
0355a3
0493ce
3277b5
9bcb3c
abd037
faa54b
f78f20
f37122
f68d4d

Requirements
Must have
• logo and necessary contact info
• Skipper Morgan Haskell
• www.tarrowferrylink.com
• morgan@tarrowferrylink.com

```html
<!DOCTYPE html>
<html lang="en">
<head>
<meta charset="utf-8">
<title>Tarrow Water Taxi and Transport Flyer</title>
<link rel="stylesheet" href="https://fonts.googleapis.com/css2?family=Exo+2:ital,wght@0,500;0,600;0,700;1,400;1,700;1,800;1,900&display=swap">
<style>
  :root {
    --navy: #0355a3;
    --sky: #0493ce;
    --pale-blue: #8fcdf2;
    --band-top: #5fb6ea;
    --band-bottom: #a7dbf7;
    --orange: #f37122;
    --orange-light: #f68d4d;
    --orange-tag: #f78f20;
    --deep-ink: #2a2e86;
    --white: #ffffff;
    --stage: #e4e7ea;
  }
  * { box-sizing: border-box; margin: 0; padding: 0; }
  html, body { width: 1200px; height: 900px; overflow: hidden; }
  body { background: var(--stage); font-family: "Exo 2", sans-serif; position: relative; }

  .flyer {
    position: absolute; left: 365px; top: 124px;
    width: 548px; height: 770px;
    transform: scale(0.86); transform-origin: top left;
    background: var(--white);
    box-shadow: 14px 14px 18px rgba(0,0,0,.35);
    overflow: hidden;
  }
  .photo { position: absolute; }
  .photo--bay      { left: 4px;   top: 4px;   width: 313px; height: 221px; background: linear-gradient(180deg,#3d8ed6 0%,#8cc4ee 48%,#e6eef5 55%,#2f6fb0 62%,#1c4f8c 100%); }
  .photo--boat     { left: 322px; top: 4px;   width: 224px; height: 221px; background: linear-gradient(180deg,#6fa9d9 0%,#4f6f86 45%,#2c3e50 70%,#4a86b8 100%); }
  .photo--sunset   { left: 4px;   top: 230px; width: 202px; height: 228px; background: linear-gradient(180deg,#7db1d6 0%,#c9b48b 38%,#f2c77a 48%,#4a5566 62%,#8a96a0 100%); }
  .photo--wake     { left: 211px; top: 230px; width: 335px; height: 228px; background: linear-gradient(180deg,#6fb7ec 0%,#a6d1ef 35%,#335e84 50%,#c7dcea 75%,#2d5a80 100%); }
  .photo--atv      { left: 4px;   top: 463px; width: 202px; height: 168px; background: linear-gradient(180deg,#5f7a5a 0%,#8a7a55 45%,#6b5c44 65%,#2d3035 100%); }
  .photo--tender   { left: 211px; top: 463px; width: 206px; height: 168px; background: linear-gradient(180deg,#2f7fd0 0%,#79b6e6 35%,#1d64b1 70%,#3a88cf 100%); }
  .photo--outboard { left: 422px; top: 463px; width: 124px; height: 168px; background: linear-gradient(180deg,#5d6570 0%,#2a2d33 50%,#7d848c 100%); }

  .title-banner {
    position: absolute; left: 138px; top: 180px;
    width: 290px; height: 128px;
    background: linear-gradient(180deg,var(--orange-light),var(--orange));
    border-radius: 8px;
    transform: rotate(5deg);
  }
  .title {
    position: absolute; left: 0; top: 0; width: 548px;
    color: var(--white); font-style: italic; font-weight: 800;
    text-shadow: 1px 2px 3px rgba(0,0,0,.35);
    line-height: 1;
  }
  .title__line1 { position: absolute; left: 50px; top: 192px; font-size: 46px; letter-spacing: -1px; white-space: nowrap; }
  .title__line2 { position: absolute; left: 172px; top: 250px; font-size: 46px; letter-spacing: -1px; white-space: nowrap; }

  .tagline {
    position: absolute; left: 306px; top: 400px;
    width: 240px; height: 113px;
    background: var(--sky);
    border: 3px solid var(--pale-blue);
    border-radius: 10px;
    padding: 17px 6px 0 14px;
    color: var(--white); font-size: 14.5px; font-weight: 500;
    line-height: 23px; text-transform: uppercase; letter-spacing: -0.2px;
  }

  .info-band {
    position: absolute; left: 0; top: 635px; width: 548px; height: 135px;
    background: linear-gradient(180deg,var(--band-top),var(--band-bottom));
  }
  .brand {
    position: absolute; left: 0; top: 47px; width: 117px; height: 88px;
    background: var(--white);
    display: flex; align-items: center; justify-content: center; gap: 5px;
  }
  .brand__dot { width: 8px; height: 8px; border-radius: 50%; background: var(--orange-tag); }
  .brand__name { color: var(--navy); font-weight: 700; font-size: 17px; letter-spacing: .5px; }

  .inside { position: absolute; left: 134px; top: 8px; width: 245px; }
  .inside__heading { color: var(--white); font-weight: 700; font-size: 22px; line-height: 30px; margin-bottom: 12px; }
  .inside__list { list-style: none; color: var(--deep-ink); font-style: italic; font-size: 10px; line-height: 18px; white-space: nowrap; }
  .inside__list li::before { content: "•"; font-style: normal; margin: 0 8px 0 0; }

  .promise {
    position: absolute; left: 384px; top: 18px; width: 148px;
    color: var(--deep-ink); font-style: italic; font-weight: 900;
    font-size: 12.5px; line-height: 14px;
  }
  .captain {
    position: absolute; left: 435px; top: 83px;
    background: var(--orange-tag); color: var(--white);
    font-size: 7.5px; font-weight: 700; padding: 2px 4px;
    border: 1px solid var(--white); white-space: nowrap;
  }
  .contact {
    position: absolute; left: 435px; top: 103px;
    color: var(--white); font-size: 6px; line-height: 9px; white-space: nowrap;
  }
</style>
</head>
<body>
  <article class="flyer">
    <div class="photo photo--bay" role="img" aria-label="Calm blue bay with snow-capped mountains on the horizon"></div>
    <div class="photo photo--boat" role="img" aria-label="Grey aluminium water taxi moored at a dock"></div>
    <div class="photo photo--sunset" role="img" aria-label="Sunset over the water seen from the boat cabin"></div>
    <div class="photo photo--wake" role="img" aria-label="Boat wake trailing across a sunlit bay"></div>
    <div class="photo photo--atv" role="img" aria-label="All-terrain vehicle unloading from the front deck onto a beach"></div>
    <div class="photo photo--tender" role="img" aria-label="Boat under way on deep blue water"></div>
    <div class="photo photo--outboard" role="img" aria-label="Twin outboard motors on the stern"></div>

    <div class="title-banner"></div>
    <h1 class="title">
      <span class="title__line1">Tarrow Water Taxi</span>
      <span class="title__line2">&amp; Transport</span>
    </h1>

    <p class="tagline">Water taxi services and freight transport in and around Kodiak Island</p>

    <section class="info-band">
      <div class="brand">
        <span class="brand__dot"></span>
        <span class="brand__name">TARROW</span>
      </div>
      <div class="inside">
        <h2 class="inside__heading">What's inside</h2>
        <ul class="inside__list">
          <li>Comfortable cabin with heat, bathroom</li>
          <li>Pick up or drop off to and from your location</li>
          <li>Surround sound stereo with blue tooth</li>
          <li>Large front deck for cargo or wild life viewing</li>
        </ul>
      </div>
      <p class="promise">All of our clients are provided with highest level of customer service</p>
      <p class="captain">Skipper Morgan Haskell</p>
      <p class="contact">tel 907-555-0148<br>email morgan@tarrowferrylink.com<br>www.tarrowferrylink.com</p>
    </section>
  </article>
</body>
</html>
```